Real estate company needs a letterhead design

A young real estate company needs a letterhead / stationery design, it should include the company's logo. It should look exactly the same as on the business cards. (With the phrase "a brand of FEO Immobilien & Projektentwicklung GmbH")

In addition, it should also include the 4 round seals.

color code blue # 00456b gray # 333333

Word and PDF are welcome.

FEO Immobilien & Projektentwicklung GmbH
Managing director: Mag. Lukas Strenhofer
Anton-Wiesmayr-Strasse 3c / 41
6300 Wörgl

Tel .: +436645917283
Email: office@wohnquell.example
Web: www.wohnquell.example

Sparkasse Almhofen, Bergländer Sparkasse from 1893, Gildenkasse
Ferdinand-Moosrainer-Strasse 9, 6300 Wörgl
IBAN: AT31 4819 2093 5521 6604
BIC: GLMRAT31XXX
Account holder: FEO Immobilien & Projektentwicklung GmbH

FN: XXXXXXX
UID: XXXXXXX

```html
<!DOCTYPE html>
<html lang="en">
<head>
<meta charset="utf-8">
<title>Wohnquell Letterhead</title>
<link href="https://fonts.googleapis.com/css2?family=Montserrat:wght@400;600;700;800&family=Encode+Sans+Condensed:wght@400&family=Lato:wght@400&display=swap" rel="stylesheet">
<style>
  :root {
    --brand-blue: #00456b;
    --ink-gray: #333333;
    --text-gray: #5a5a5a;
    --soft-gray: #6e6e6e;
    --seal-fill: #eef3f6;
    --paper: #ffffff;
  }
  * { margin: 0; padding: 0; box-sizing: border-box; }
  html, body { width: 1056px; height: 1200px; overflow: hidden; background: var(--paper); }
  .letterhead {
    position: relative;
    width: 1056px;
    height: 1200px;
    background: var(--paper);
    font-family: "Montserrat", sans-serif;
    color: var(--text-gray);
  }

  /* Brand block */
  .brand { position: absolute; left: 99px; top: 112px; }
  .brand-row { display: flex; align-items: center; gap: 12px; }
  .brand-mark { width: 30px; height: 30px; background: var(--brand-blue); flex: none; }
  .brand-name {
    font-family: "Montserrat", sans-serif;
    font-weight: 600;
    font-size: 36px;
    color: var(--brand-blue);
    line-height: 1;
  }
  .brand-tagline {
    margin-top: 12px;
    font-family: "Lato", sans-serif;
    font-size: 12.5px;
    color: var(--ink-gray);
  }

  /* Seals */
  .seals { position: absolute; left: 99px; top: 236px; display: flex; gap: 14px; }
  .seal {
    width: 52px; height: 52px; border-radius: 50%;
    background: var(--seal-fill);
    border: 2px solid var(--brand-blue);
  }

  /* Sender block */
  .sender { position: absolute; left: 705px; top: 50px; width: 330px; }
  .sender-name { font-size: 21px; font-weight: 700; color: var(--brand-blue); line-height: 1.2; }
  .sender-role { font-size: 14.5px; color: var(--soft-gray); margin-top: 1px; }
  .sender-address { font-size: 14.5px; color: var(--soft-gray); margin-top: 9px; line-height: 1.25; }
  .contact-list { list-style: none; margin-top: 8px; }
  .contact-list li {
    display: flex; align-items: center; gap: 14px;
    font-size: 14.5px; color: var(--soft-gray); height: 19px;
  }
  .contact-list svg { width: 15px; height: 15px; flex: none; }
  .bank-list { list-style: none; margin-top: 8px; }
  .bank-list li { font-size: 14.5px; color: var(--soft-gray); height: 21.5px; }
  .bank-list b { color: var(--brand-blue); font-weight: 700; }

  /* Recipient */
  .date { position: absolute; left: 99px; top: 432px; font-size: 19px; font-weight: 400; color: var(--text-gray); }
  .recipient { position: absolute; left: 99px; top: 463px; }
  .recipient-name { font-size: 33px; font-weight: 800; color: var(--text-gray); letter-spacing: 0.3px; line-height: 1.1; }
  .recipient-role { font-size: 19px; color: var(--text-gray); margin-top: 6px; }

  /* Body */
  .body-copy {
    position: absolute; left: 99px; top: 582px; width: 865px;
    font-family: "Encode Sans Condensed", sans-serif;
    font-size: 20px; line-height: 29px; color: var(--text-gray);
    text-align: justify;
  }
  .body-copy p + p { margin-top: 29px; }

  .closing {
    position: absolute; left: 99px; top: 906px;
    font-family: "Encode Sans Condensed", sans-serif;
    font-size: 20px; color: var(--text-gray);
  }
  .signature {
    position: absolute; left: 99px; top: 952px; width: 146px; height: 58px;
    background: linear-gradient(90deg, #e7eef3, #f4f7f9);
    border-radius: 4px;
  }

  /* Footer */
  .footer { position: absolute; left: 0; right: 0; top: 1108px; text-align: center; }
  .footer-company { font-size: 17px; font-weight: 700; color: var(--brand-blue); }
  .footer-bank {
    font-family: "Lato", sans-serif;
    font-size: 16.5px; color: var(--soft-gray); line-height: 21px; margin-top: 4px;
  }
</style>
</head>
<body>
<main class="letterhead">

  <header class="brand">
    <div class="brand-row">
      <span class="brand-mark" aria-hidden="true"></span>
      <span class="brand-name">WOHNQUELL</span>
    </div>
    <div class="brand-tagline">eine Marke der F E O Immobilien &amp; Projektentwicklung GmbH</div>
  </header>

  <div class="seals" role="img" aria-label="Four round quality seals">
    <span class="seal"></span>
    <span class="seal"></span>
    <span class="seal"></span>
    <span class="seal"></span>
  </div>

  <section class="sender">
    <div class="sender-name">Mag. Lukas Strenhofer</div>
    <div class="sender-role">Managing director</div>
    <div class="sender-address">Anton-Wiesmayr-Strasse<br>3c / 41 6300 Wörgl</div>
    <ul class="contact-list">
      <li>
        <svg viewBox="0 0 16 16" aria-hidden="true"><path d="M3.5 1.5l2.3 2.6-1.3 1.7c.9 2 2.5 3.6 4.5 4.5l1.7-1.3 2.6 2.3-1.2 2c-5.2-.4-9.5-4.7-9.9-9.9z" fill="var(--brand-blue)"/><path d="M10 2.5a4 4 0 0 1 3.5 3.5M10 .8a5.8 5.8 0 0 1 5.2 5.2" stroke="var(--brand-blue)" stroke-width="1.2" fill="none"/></svg>
        +436645917283
      </li>
      <li>
        <svg viewBox="0 0 16 16" aria-hidden="true"><rect x="1" y="3.5" width="14" height="9" fill="var(--brand-blue)"/><path d="M1.5 4l6.5 5 6.5-5M1.5 12l5-4M14.5 12l-5-4" stroke="#fff" stroke-width="1.1" fill="none"/></svg>
        office@wohnquell.example
      </li>
      <li>
        <svg viewBox="0 0 16 16" aria-hidden="true"><g stroke="var(--brand-blue)" stroke-width="1" fill="none"><circle cx="8" cy="8" r="6.5"/><ellipse cx="8" cy="8" rx="3" ry="6.5"/><path d="M1.5 8h13M2.5 4.7h11M2.5 11.3h11M8 1.5v13"/></g></svg>
        www.wohnquell.example
      </li>
    </ul>
    <ul class="bank-list">
      <li><b>IBAN:</b> AT31 4819 2093 5521 6604</li>
      <li><b>BIC:</b> GLMRAT31XXX</li>
      <li><b>FN:</b> XXXXXXX</li>
      <li><b>UID:</b> XXXXXXX</li>
    </ul>
  </section>

  <div class="date">10 December, 2021</div>
  <section class="recipient">
    <div class="recipient-name">THOMAS REINER</div>
    <div class="recipient-role">Cheif Executive Officer</div>
  </section>

  <article class="body-copy">
    <p>Contrary to popular belief, Lorem Ipsum is not simply random text. It has roots in a piece of classical Latin literature from 45 BC, making it over 2000 years old. Henry Caldwell, a Latin professor at Ashbury Hill College in Virginia, looked up one of the more obscure Latin words, consectetur.</p>
    <p>Lorem Ipsum comes from sections 1.10.32 and 1.10.33 of "de Finibus Bonorum et Malorum" (The Extremes of Good and Evil) by Aurelius, written in 45 BC. This book is a treatise on the theory of ethics, very popular during the Renaissance. The first line of Lorem Ipsum.</p>
    <p>The standard chunk of Lorem Ipsum used since the 1500s is reproduced below for those interested.</p>
  </article>

  <div class="closing">Best Regards</div>
  <div class="signature" role="img" aria-label="Handwritten signature of Lukas in blue ink"></div>

  <footer class="footer">
    <div class="footer-company">FEO Immobilien &amp; Projektentwicklung GmbH</div>
    <div class="footer-bank">Sparkasse Almhofen, Bergländer Sparkasse from 1893, Gildenkasse<br>Ferdinand-Moosrainer-Strasse 9, 6300 Wörgl</div>
  </footer>

</main>
</body>
</html>
```